New Property management company business cards

Looking for a new business card, to reflect new younger ownership
Card should be clean, simple and professional but with a modern layout that is conveys our new logo and business model

Key aspects of the business:

Property Management
Facility Maintenance
Project Management
Tenant Improvements

Mailing Address:
PO BOX 7186
Lindale CA, 95481

Phone: 209-614-8837
Direct: 209-614-8831

Doyle Farrant
President

Target Market(s)

Commercial property owners

Industry/Entity Type

Real Estate property management

Contact Information for Business Card

Open to all designs but lean toward vertical layouts

Requirements
Must have
• Logo and space to customize name and contact info

```html
<!DOCTYPE html>
<html lang="en">
<head>
<meta charset="utf-8">
<title>Marlowe Property Management – Business Card</title>
<link href="https://fonts.googleapis.com/css2?family=Montserrat:wght@500;600;700&display=swap" rel="stylesheet">
<style>
  :root {
    --backdrop: #d1d2d4;
    --paper: #ffffff;
    --ink: #343341;
    --teal: #22aca8;
  }
  * { margin: 0; padding: 0; box-sizing: border-box; }
  html, body {
    width: 1200px; height: 1199px; overflow: hidden;
    background: var(--backdrop);
    font-family: "Montserrat", Arial, sans-serif;
  }
  .card {
    position: absolute; left: 181px; width: 837px; height: 478px;
    background: var(--paper); overflow: hidden;
  }
  .card--front { top: 83px; }
  .card--back { top: 637px; }
  .card__art { position: absolute; inset: 0; width: 100%; height: 100%; }

  .brand { position: absolute; display: flex; align-items: center; color: var(--ink); font-weight: 600; }
  .brand__square { background: var(--teal); flex: none; }
  .brand__text { line-height: 1; }
  .brand__sub { display: block; letter-spacing: 0.42em; margin-top: 6px; }

  .brand--front { left: 32px; top: 62px; gap: 12px; }
  .brand--front .brand__square { width: 34px; height: 34px; }
  .brand--front .brand__name { font-size: 34px; letter-spacing: 0.18em; }
  .brand--front .brand__sub { font-size: 9px; }

  .brand--back { left: 103px; top: 190px; gap: 20px; }
  .brand--back .brand__square { width: 58px; height: 58px; }
  .brand--back .brand__name { font-size: 54px; letter-spacing: 0.18em; }
  .brand--back .brand__sub { font-size: 14px; margin-top: 9px; }

  .person { position: absolute; left: 32px; top: 190px; }
  .person__name { font-size: 38px; font-weight: 700; color: var(--ink); letter-spacing: 0.01em; line-height: 1; }
  .person__title { display: flex; align-items: center; gap: 26px; margin-top: 6px; font-size: 20px; font-weight: 700; color: var(--teal); letter-spacing: 0.03em; }
  .person__rule { width: 101px; height: 3px; background: var(--teal); }

  .contact { position: absolute; color: var(--paper); font-weight: 700; font-size: 12px; letter-spacing: 0.14em; line-height: 15.5px; }
  .contact--phone { left: 37px; top: 341px; display: flex; gap: 19px; align-items: center; }
  .contact--phone svg { width: 20px; height: 20px; }
  .contact--mail { left: 39px; top: 396px; }
  .contact__heading { font-size: 17px; font-weight: 600; letter-spacing: 0.06em; margin-bottom: 10px; line-height: 1.2; }
  .services { position: absolute; left: 371px; top: 353px; color: var(--paper); font-weight: 700; font-size: 12px; letter-spacing: 0.13em; line-height: 15px; }
  .services__heading { font-size: 16px; font-weight: 600; letter-spacing: 0.08em; margin-bottom: 15px; line-height: 1.2; }
  .services__list { list-style: none; }
</style>
</head>
<body>
  <section class="card card--front">
    <svg class="card__art" viewBox="0 0 1348 770" preserveAspectRatio="none" aria-hidden="true">
      <polygon fill="var(--ink)" points="0,482 866,482 1348,0 1348,140 976,513 0,513"/>
      <polygon fill="var(--teal)" points="0,513 1090,513 1348,256 1348,396 1230,513 1348,630 1348,770 0,770"/>
    </svg>

    <div class="brand brand--front">
      <span class="brand__square"></span>
      <span class="brand__text"><span class="brand__name">MARLOWE</span><span class="brand__sub">PROPERTY MANAGEMENT</span></span>
    </div>

    <div class="person">
      <h1 class="person__name">DOYLE FARRANT</h1>
      <p class="person__title">PRESIDENT <span class="person__rule"></span></p>
    </div>

    <div class="contact contact--phone">
      <svg viewBox="0 0 24 24" aria-hidden="true"><path fill="#fff" d="M6.6 10.8c1.4 2.8 3.8 5.1 6.6 6.6l2.2-2.2c.3-.3.7-.4 1-.2 1.1.4 2.3.6 3.6.6.6 0 1 .4 1 1V20c0 .6-.4 1-1 1C10.6 21 3 13.4 3 4c0-.6.4-1 1-1h3.5c.6 0 1 .4 1 1 0 1.3.2 2.5.6 3.6.1.3 0 .7-.2 1L6.6 10.8z"/></svg>
      <p>209-614-8837<br>209-614-8831</p>
    </div>

    <div class="contact contact--mail">
      <p class="contact__heading">Mailing Address:</p>
      <p>PO BOX 7186<br>LINDALE CA, 95481</p>
    </div>

    <div class="services">
      <p class="services__heading">SERVICES:</p>
      <ul class="services__list">
        <li>•PROPERTY MANAGEMENT</li>
        <li>•FACILITY MAINTENANCE</li>
        <li>•PROJECT MANAGEMENT</li>
        <li>•TENANT IMPROVEMENTS</li>
      </ul>
    </div>
  </section>

  <section class="card card--back">
    <svg class="card__art" viewBox="0 0 1348 770" preserveAspectRatio="none" aria-hidden="true">
      <polygon fill="var(--ink)" points="834,512 974,512 1348,139 1348,0"/>
      <polygon fill="var(--teal)" points="1090,512 1348,256 1348,396 1230,512 1348,630 1348,770"/>
    </svg>

    <div class="brand brand--back">
      <span class="brand__square"></span>
      <span class="brand__text"><span class="brand__name">MARLOWE</span><span class="brand__sub">PROPERTY MANAGEMENT</span></span>
    </div>
  </section>
</body>
</html>
```